Upscale business cards needed for family business

We need professional business cards created for several family members. We are a family business holding company. We would like these relatively simple and straightforward, but also with a unique element to set them apart. Probably stick with neutral and simple colors - white, grey etc. We need space for the traditional elements, including name, title, address, email/phone number. And we will be creating several from this template so it needs to be template that is easy to switch information in and out of.

Industry/Entity Type

Business

Contact Information for Business Card

Please include the attached Marwood Capital logo.

Requirements
Must have
• The attached Marwood Capital logo.

```html
<!DOCTYPE html>
<html lang="en">
<head>
<meta charset="utf-8">
<title>Marwood Capital – Business Card</title>
<link rel="stylesheet" href="https://fonts.googleapis.com/css2?family=Cinzel:wght@500;600&family=Open+Sans:wght@400&display=swap">
<style>
  :root {
    --backdrop: #3b3b3b;
    --card-light: #ffffff;
    --card-dark: #141617;
    --gold: #c6932b;
    --ink: #222222;
    --ink-soft: #5a5a5a;
    --divider: #c9c9c9;
    --white: #f4f4f4;
  }
  * { margin: 0; padding: 0; box-sizing: border-box; }
  html, body { width: 1105px; height: 1200px; overflow: hidden; }
  body { background: var(--backdrop); position: relative; font-family: "Open Sans", Arial, sans-serif; }

  .card { position: absolute; left: 196px; width: 720px; height: 411px; }
  .card--front { top: 146px; background: var(--card-light); }
  .card--back { top: 602px; background: var(--card-dark); }

  .brand-name {
    font-family: "Cinzel", Georgia, serif;
    font-weight: 500;
    letter-spacing: 0.5px;
    white-space: nowrap;
    position: absolute;
    transform: translateX(-50%);
    text-align: center;
  }
  .card--front .brand-name { left: 200px; top: 188px; font-size: 27px; color: var(--ink); }
  .card--back .brand-name { left: 360px; top: 222px; font-size: 36px; color: var(--white); }

  .divider { position: absolute; left: 377px; top: 95px; width: 1px; height: 228px; background: var(--divider); }

  .contact { position: absolute; left: 408px; top: 96px; }
  .contact__name { font-family: "Cinzel", Georgia, serif; font-weight: 600; font-size: 28px; color: var(--gold); line-height: 1.1; letter-spacing: 0.5px; }
  .contact__title { font-size: 19px; color: var(--ink); margin-top: 2px; }
  .contact__address { font-size: 18px; color: var(--ink-soft); margin-top: 18px; line-height: 26px; }
  .contact__list { list-style: none; margin-top: 6px; }
  .contact__item { display: flex; align-items: center; font-size: 18px; color: var(--ink-soft); line-height: 27.5px; }
  .contact__icon { width: 16px; height: 16px; margin-right: 10px; fill: var(--gold); flex: none; }

  .website { position: absolute; left: 0; right: 0; top: 334px; text-align: center; font-size: 18px; color: var(--white); letter-spacing: 1.5px; }
</style>
</head>
<body>
  <section class="card card--front">
    <div class="brand-name">Marwood Capital Inc</div>
    <div class="divider"></div>
    <div class="contact">
      <h1 class="contact__name">Daniel Arden</h1>
      <p class="contact__title">CEO/Founder</p>
      <p class="contact__address">4120 Larkspur Court<br>Juneau, Alaska 99801</p>
      <ul class="contact__list">
        <li class="contact__item">
          <svg class="contact__icon" viewBox="0 0 16 16" aria-hidden="true"><path d="M3.6 1.2l2.2 2.9-1.3 1.6c.9 2 2.2 3.3 4.2 4.3l1.6-1.3 2.9 2.2-1.4 2.6C7 13.2 2.8 9 1.2 3.9z"/></svg>
          907 555 0148
        </li>
        <li class="contact__item">
          <svg class="contact__icon" viewBox="0 0 16 16" aria-hidden="true"><path d="M1 4h14v1.2L8 9.3 1 5.2z"/><path d="M1 6.6l7 4 7-4V12H1z"/></svg>
          daniel@marwoodcap.com
        </li>
        <li class="contact__item">
          <svg class="contact__icon" viewBox="0 0 16 16" aria-hidden="true"><circle cx="8" cy="8" r="7"/><path d="M5 4.5c1.5.3 2 1.5 1.2 2.5-.8.9.4 2 1.4 1.6 1-.3 1.5 1 1 2.2-.4 1 .3 1.8 1.3 1.5" stroke="#fff" stroke-width="1.3" fill="none"/></svg>
          www.marwoodcap.com
        </li>
      </ul>
    </div>
  </section>

  <section class="card card--back">
    <div class="brand-name">Marwood Capital Inc</div>
    <p class="website">www.marwoodcapitalinc.com</p>
  </section>
</body>
</html>
```